Design a letterhead and business card for a Mosaic Company

Please refer to the attached document for the details to be included in the letterhead and business cards. Logo and contact details enclosed therein. Client is looking for a professional image.
Please include as many contact details as possible in your entries.
Please see updated .AI and .PNG images.

```html
<!DOCTYPE html>
<html lang="en">
<head>
<meta charset="utf-8">
<title>Tessera Works – Business Card</title>
<link rel="stylesheet" href="https://fonts.googleapis.com/css2?family=Arimo:wght@400;700&family=Michroma&display=swap">
<style>
  :root {
    --backdrop: #a8a8a8;
    --card: #ffffff;
    --ink: #1d1d1d;
    --ink-soft: #444444;
    --band: #7c7c7c;
    --band-edge: #231f20;
    --tagline: #ffffff;
  }
  * { box-sizing: border-box; margin: 0; padding: 0; }
  html, body {
    width: 1200px;
    height: 554px;
    overflow: hidden;
    background: var(--backdrop);
  }
  .canvas {
    position: relative;
    width: 1200px;
    height: 554px;
  }
  .card {
    position: absolute;
    top: 143px;
    width: 524px;
    height: 299px;
    background: var(--card);
    overflow: hidden;
  }
  .card--front { left: 68px; }
  .card--back { left: 606px; }

  .holder-name {
    position: absolute;
    top: 24px;
    left: 0;
    width: 100%;
    text-align: center;
    font-family: "Michroma", sans-serif;
    font-size: 17px;
    color: var(--ink);
  }
  .contact-line {
    position: absolute;
    left: 0;
    width: 100%;
    display: flex;
    justify-content: center;
    align-items: center;
    gap: 6px;
    font-family: "Arimo", sans-serif;
    font-size: 12.5px;
    color: var(--ink-soft);
  }
  .contact-line--first { top: 55px; }
  .contact-line--second { top: 76px; }
  .contact-item { display: inline-flex; align-items: center; gap: 4px; }
  .contact-item svg { width: 14px; height: 12px; fill: var(--ink); }

  .company-front {
    position: absolute;
    top: 140px;
    left: 0;
    width: 100%;
    text-align: center;
    font-family: "Arimo", sans-serif;
    font-weight: 700;
    font-size: 30px;
    letter-spacing: 1px;
    color: var(--ink);
  }
  .tagline-band {
    position: absolute;
    left: 0;
    bottom: 0;
    width: 100%;
    height: 46px;
    background: var(--band);
    border-top: 4px solid var(--band-edge);
    display: flex;
    align-items: center;
    justify-content: center;
  }
  .tagline {
    font-family: "Arimo", sans-serif;
    font-weight: 700;
    font-size: 13px;
    letter-spacing: 0.5px;
    color: var(--tagline);
    word-spacing: 3px;
  }

  .brand {
    position: absolute;
    top: 0;
    left: 0;
    width: 100%;
    height: 100%;
    display: flex;
    align-items: center;
    justify-content: center;
    gap: 12px;
  }
  .brand-square {
    width: 26px;
    height: 26px;
    background: var(--ink);
  }
  .brand-name {
    font-family: "Arimo", sans-serif;
    font-weight: 700;
    font-size: 30px;
    letter-spacing: 1px;
    color: var(--ink);
  }
</style>
</head>
<body>
<main class="canvas">
  <section class="card card--front">
    <h1 class="holder-name">Lena Marsh</h1>
    <div class="contact-line contact-line--first">
      <span class="contact-item">
        <svg viewBox="0 0 14 12" aria-hidden="true"><path d="M1 3 Q7 -1 13 3 L12 5 L10 4 L10 3 Q7 2 4 3 L4 4 L2 5 Z M3 6 L11 6 L12 11 L2 11 Z"/></svg>
        072 5550194
      </span>
      <span class="contact-item">
        <svg viewBox="0 0 14 12" aria-hidden="true"><path d="M1 2 H13 V10 H1 Z M2 3 L7 7 L12 3" fill="none" stroke="#1d1d1d" stroke-width="1.4"/></svg>
        hello@tesseraworks.co.za
      </span>
    </div>
    <div class="contact-line contact-line--second">
      <span class="contact-item">
        <svg viewBox="0 0 14 12" aria-hidden="true"><g fill="none" stroke="#1d1d1d" stroke-width="1"><circle cx="7" cy="6" r="5"/><ellipse cx="7" cy="6" rx="2.2" ry="5"/><path d="M2 6 H12 M3 3.5 H11 M3 8.5 H11"/></g></svg>
        www.tesseraworks.co.za
      </span>
    </div>
    <p class="company-front">TESSERA WORKS</p>
    <div class="tagline-band">
      <p class="tagline">YOU ENVISION IT AND I WILL CREATE IT</p>
    </div>
  </section>

  <section class="card card--back">
    <div class="brand">
      <span class="brand-square"></span>
      <span class="brand-name">TESSERA WORKS</span>
    </div>
  </section>
</main>
</body>
</html>
```